Flight school needs business cards!

We need a cool business card design for two flight school employees. The Chief Flight Instructor and the Manager. Put simply, we teach people how to fly. I would think it would be cool to have the front of the business card look like a pilot's license (US pilot certificate) and the backside has the logo and contact information.

Target Market(s)

Someone who wants to learn how to fly.

Industry/Entity Type

Aviation

Requirements
Must have
• The front of the business card should look like a United States pilot license, and it should read:

Your Name Here
Your Address Here

DOB and other personal information should be left plank.

Then under where it says
"Has been found to be properly qualified to exercise the privileges of
It should say Sport Pilot
Private Pilot
Commercial pilot

Basically, it is a way of saying what types of pilot licenses we can train someone for, and should be motivating for someone to have in their wallet. Something they don't want to throw away

```html
<!DOCTYPE html>
<html lang="en">
<head>
<meta charset="utf-8">
<title>Pilot Certificate Business Card</title>
<link href="https://fonts.googleapis.com/css2?family=Arimo:wght@400;700&display=swap" rel="stylesheet">
<style>
  :root {
    --backdrop: #262626;
    --backdrop-edge: #0e0e0e;
    --card-blue: #bccbdd;
    --card-teal: #8db6c0;
    --card-sand: #d0bf95;
    --ink: #1d2226;
    --faint-line: rgba(55, 75, 90, 0.13);
    --faint-fill: rgba(55, 75, 90, 0.08);
    --badge-navy: #1d2d5e;
    --badge-red: #c7343a;
    --seal-gold: #c9a23a;
  }
  * { margin: 0; padding: 0; box-sizing: border-box; }
  html, body { width: 1200px; height: 900px; overflow: hidden; }
  body {
    background: radial-gradient(ellipse at center, var(--backdrop) 0%, var(--backdrop-edge) 100%);
    font-family: "Arimo", Arial, sans-serif;
    color: var(--ink);
    position: relative;
  }
  .certificate-card {
    position: absolute;
    left: 200px; top: 200px;
    width: 800px; height: 500px;
    border-radius: 44px;
    overflow: hidden;
    background: linear-gradient(115deg, var(--card-blue) 0%, var(--card-teal) 55%, var(--card-sand) 100%);
    box-shadow: 0 10px 30px rgba(0,0,0,0.6);
  }
  .watermark-art {
    position: absolute;
    left: 40px; top: 20px;
    width: 740px; height: 470px;
  }
  .holder-name, .holder-address {
    position: absolute;
    left: 150px;
    font-weight: 700;
    font-size: 24px;
    letter-spacing: 0.5px;
  }
  .holder-name { top: 62px; }
  .holder-address { top: 112px; }
  .personal-details {
    position: absolute;
    left: 95px; top: 176px;
    font-weight: 700;
    font-size: 14px;
    line-height: 20px;
  }
  .physical-fields {
    position: absolute;
    left: 440px; top: 218px;
    font-weight: 700;
    font-size: 19px;
    word-spacing: 12px;
  }
  .privileges-line {
    position: absolute;
    left: 95px; top: 258px;
    font-weight: 700;
    font-size: 15px;
    letter-spacing: 0.2px;
  }
  .ratings {
    position: absolute;
    left: 95px; top: 300px;
    font-weight: 700;
    font-size: 22px;
    line-height: 32px;
    display: grid;
    grid-template-columns: 44px auto;
  }
  .issuer-seal {
    position: absolute;
    left: 440px; top: 380px;
    width: 76px; height: 76px;
  }
  .school-mark {
    position: absolute;
    left: 640px; top: 300px;
    width: 130px;
    text-align: center;
  }
  .school-mark svg { display: block; margin: 0 auto 8px; }
  .school-name {
    font-weight: 700;
    font-size: 15px;
    letter-spacing: 1px;
    color: var(--ink);
  }
</style>
</head>
<body>
  <div class="certificate-card">
    <svg class="watermark-art" viewBox="0 0 740 470" role="img" aria-label="Faint aircraft and transportation seal watermark">
      <circle cx="450" cy="270" r="200" fill="var(--faint-fill)"/>
      <circle cx="450" cy="270" r="200" fill="none" stroke="var(--faint-line)" stroke-width="3"/>
      <circle cx="450" cy="270" r="150" fill="none" stroke="var(--faint-line)" stroke-width="2"/>
    </svg>

    <div class="holder-name">YOUR NAME HERE</div>
    <div class="holder-address">YOUR ADDRESS HERE</div>

    <div class="personal-details">
      <p>VI NATIONALITY USA</p>
      <p>IVA D.O.B.</p>
    </div>

    <div class="physical-fields">SEX HEIGHT WEIGHT HAIR EYES</div>

    <div class="privileges-line">IX HAS BEEN FOUND TO BE PROPERLY QUALIFIED TO EXERCISE THE PRIVILEGES OF</div>

    <div class="ratings">
      <span>I</span><span>SPORT PILOT</span>
      <span>II</span><span>PRIVATE PILOT</span>
      <span>III</span><span>COMMERCIAL PILOT</span>
    </div>

    <svg class="issuer-seal" viewBox="0 0 76 76" aria-hidden="true">
      <circle cx="38" cy="38" r="37" fill="var(--seal-gold)"/>
      <circle cx="38" cy="38" r="31" fill="var(--badge-navy)"/>
    </svg>

    <div class="school-mark">
      <svg width="86" height="86" viewBox="0 0 86 86" aria-hidden="true">
        <circle cx="43" cy="43" r="40" fill="var(--badge-navy)" stroke="var(--badge-red)" stroke-width="4"/>
      </svg>
      <div class="school-name">ZENITH AVIATION</div>
    </div>
  </div>
</body>
</html>
```